exclusive Speakeasy Bar Web design in New Jersey USA

We are opening a speakeasy in New Jersey USA soon. we are looking for a web designer to do our web site including the coding. we a looking for a 4 to 5 page web design. the site will be mostly static. home page, contact page, menu page and a link to a 3rd party site (most likely Qelmo) for reservations. we are looking for this designer to do our menu deign as well. we are looking for a quick turnaround 7-10 days. i am attaching some pictures for the designers to see the concept design and the actual current pictures with our logo as well. professionally taken pictures will be provided later on. our photographer will be taking the pictures in the next week.

Industry/Entity Type

Restaurant, Bar, Speakeasy

Coding

Coded - Design and coding required

Number of Pages Required

4 page

Requirements
Must have
• home page, contact page, menu page and a link to qelmo.com for reservations
Nice to have
• some videos

```html
<!DOCTYPE html>
<html lang="en">
<head>
<meta charset="utf-8">
<title>Velvet Lantern — Speakeasy</title>
<link href="https://fonts.googleapis.com/css2?family=Playfair+Display:wght@400;600&family=Montserrat:wght@400;500;600&display=swap" rel="stylesheet">
<style>
:root{
  --ink:#0f0f0f;
  --ink-soft:#1b1b1b;
  --gold:#a9812f;
  --gold-light:#c9a55a;
  --paper:#ecebe6;
  --white:#ffffff;
  --muted:#bdbdbd;
  --serif:'Playfair Display', Georgia, serif;
  --sans:'Montserrat', Arial, sans-serif;
}
*{box-sizing:border-box;margin:0;padding:0}
html,body{width:1200px;height:2836px;overflow:hidden;background:var(--ink);font-family:var(--sans);color:var(--white)}
.page{position:relative;width:1200px;height:2836px}

/* hero */
.hero{position:absolute;left:0;top:0;width:1200px;height:792px;
  background:linear-gradient(180deg,#1d1a17 0%,#3a2f24 38%,#4a3a2a 60%,#23201d 100%)}
.hero::after{content:"";position:absolute;inset:0;background:rgba(0,0,0,.35)}
.topbar{position:absolute;top:14px;left:0;width:100%;z-index:2;font-size:11px;color:var(--muted)}
.topbar .left{position:absolute;left:128px;display:flex;gap:36px}
.topbar .right{position:absolute;right:120px;display:flex;gap:26px}
.nav{position:absolute;top:62px;z-index:2;display:flex;gap:44px;font-size:14px;letter-spacing:1px;text-transform:uppercase}
.nav a{color:var(--white);text-decoration:none}
.nav.left{left:210px}
.nav.right{right:190px}
.nav a.active{color:var(--gold-light);border-bottom:1px solid var(--gold-light);padding-bottom:6px}
.brand-box{position:absolute;left:528px;top:0;width:144px;height:190px;background:var(--white);z-index:3;
  display:flex;flex-direction:column;align-items:center;justify-content:center;gap:8px}
.brand-box .mark{width:14px;height:14px;background:var(--gold)}
.brand-box .name{font-family:var(--serif);color:var(--ink);font-size:22px;line-height:1.15;text-align:center}
.hero-copy{position:absolute;top:300px;left:0;width:100%;text-align:center;z-index:2}
.hero-copy .kicker{font-family:var(--serif);font-size:42px}
.hero-copy h1{font-family:var(--serif);font-weight:400;font-size:76px;line-height:1.1}
.play{display:block;margin:22px auto 0}
.btn{display:inline-block;background:var(--gold);color:var(--white);font-size:15px;letter-spacing:1px;
  text-transform:uppercase;padding:15px 32px;text-decoration:none}
.hero-copy .btn{margin-top:28px}

/* intro */
.intro-card{position:absolute;left:0;top:800px;width:580px;height:410px;background:var(--gold);padding:90px 64px 0 28px}
.intro-card h2{font-family:var(--serif);font-weight:400;font-size:32px;line-height:1.15;text-transform:uppercase}
.intro-card p{margin-top:20px;font-size:13px;line-height:1.55;color:#f3ead6;max-width:470px}
.bar-photo{position:absolute;left:580px;top:800px;width:620px;height:670px;
  background:linear-gradient(160deg,#2a2320 0%,#6b4a2a 45%,#3a2c22 75%,#1b1715 100%)}
.frame-line{position:absolute;border:2px solid rgba(255,255,255,.75)}
.hours{position:absolute;left:0;top:1210px;width:580px;height:260px;background:var(--paper);color:var(--ink);padding:70px 0 0 120px}
.hours h3{font-family:var(--serif);font-weight:400;font-size:32px;text-transform:uppercase}
.hours p{font-size:13px;margin-top:22px}
.hours p + p{margin-top:18px}

/* drinks */
.drinks{position:absolute;left:0;top:1470px;width:1200px;height:510px;background:var(--ink)}
.drinks-photo{position:absolute;left:112px;top:80px;width:508px;height:340px;
  background:linear-gradient(135deg,#3a3a3a 0%,#7a7a7a 45%,#2a2a2a 100%)}
.drinks-copy{position:absolute;left:716px;top:124px;width:400px}
.drinks-copy h2{font-family:var(--serif);font-weight:400;font-size:30px;line-height:1.2;text-transform:uppercase}
.drinks-copy p{margin-top:16px;font-size:13px;line-height:1.55;color:var(--muted)}
.drinks-copy .btn{margin-top:24px}

/* location */
.location{position:absolute;left:0;top:1980px;width:1200px;height:580px;background:var(--paper);color:var(--ink)}
.map{position:absolute;left:112px;top:72px;width:468px;height:408px;background:linear-gradient(135deg,#e4e2dc,#d7d3c8)}
.location-copy{position:absolute;left:686px;top:178px}
.location-copy h2{font-family:var(--serif);font-weight:400;font-size:32px;text-transform:uppercase}
.location-copy .phone{margin-top:16px;font-size:16px;font-weight:600}
.location-copy address{font-style:normal;margin-top:6px;font-size:16px;line-height:1.35;text-transform:uppercase;max-width:300px}
.location-copy .btn{margin-top:22px}

/* footer */
.footer{position:absolute;left:0;top:2560px;width:1200px;height:276px;background:var(--ink-soft)}
.footer-frame{position:absolute;left:80px;top:40px;width:1040px;height:190px;border:1px solid #6a6a6a}
.footer-links{position:absolute;left:44px;top:50px;list-style:none;font-size:14px;line-height:1.7;text-transform:uppercase}
.footer-links li:first-child{color:var(--gold-light)}
.footer-brand{position:absolute;left:480px;top:0;width:80px;height:190px;border-left:1px solid #6a6a6a;border-right:1px solid #6a6a6a;
  display:flex;align-items:center;justify-content:center}
.footer-brand .name{font-family:var(--serif);font-size:14px;writing-mode:vertical-rl;transform:rotate(180deg);letter-spacing:1px}
.footer-social{position:absolute;right:40px;top:52px;text-align:right;font-size:13px;text-transform:uppercase}
.footer-social .icons{display:flex;gap:12px;justify-content:flex-end;margin-top:14px}
.footer-social .icons span{width:16px;height:16px;border-radius:50%;background:var(--gold)}
.footer-social .copy{margin-top:20px;font-size:11px;text-transform:none;color:var(--muted)}
</style>
</head>
<body>
<div class="page">

  <header class="hero" role="img" aria-label="Photo of the dim speakeasy bar interior with leather seats and hanging lamps">
    <div class="topbar">
      <div class="left"><span>Open (4): 5:00 PM To 2:00 AM</span><span>info@velvetlantern.com</span></div>
      <div class="right"><span>27 Ferry Lane, Hoboken, NJ</span><span>1 (555) 014 2290</span></div>
    </div>
    <nav class="nav left"><a class="active" href="#">Home</a><a href="#">Menu</a></nav>
    <nav class="nav right"><a href="#">Contact</a><a href="https://qelmo.com">Reservations</a></nav>
    <div class="brand-box"><span class="mark"></span><span class="name">Velvet<br>Lantern</span></div>
    <div class="hero-copy">
      <div class="kicker">Welcome to</div>
      <h1>Velvet Lantern</h1>
      <svg class="play" width="40" height="40" viewBox="0 0 40 40" aria-hidden="true">
        <circle cx="20" cy="20" r="17" fill="none" stroke="#fff" stroke-width="2.5"/>
        <path d="M16 13 L28 20 L16 27 Z" fill="#fff"/>
      </svg>
      <a class="btn" href="https://qelmo.com">Reservation Now</a>
    </div>
  </header>

  <section class="intro-card">
    <h2>A taste of the countryside in the heart of the city</h2>
    <p>Lorem ipsum dolor sit amet consectetur. Etiam eros aenean malesuada nibh volutpat natoque. Porta at vel imperdiet nisl tempus posuere. Hendrerit tincidunt lectus diam pulvinar erat est praesent ipsum. Elementum aliquam dictum mi tellus et. Tellus integer odio et est et tristique quam ut.</p>
  </section>

  <div class="bar-photo" role="img" aria-label="Photo of back-bar shelves lined with liquor bottles">
    <div class="frame-line" style="left:40px;top:30px;width:540px;height:600px"></div>
  </div>

  <section class="hours">
    <h3>Open Daily</h3>
    <p>Sunday – Thursday: 11am – 11pm</p>
    <p>Friday &amp; Saturday: 11am – 2am</p>
  </section>

  <section class="drinks">
    <div class="drinks-photo" role="img" aria-label="Black and white photo of cocktails with gold script lettering overlay"></div>
    <div class="drinks-copy">
      <h2>Food, drinks &amp; the best atmosphere in town</h2>
      <p>Good beer brings people together. That's why every one of our beers is crafted with the simple purpose of helping people spend meaningful time with each other</p>
      <a class="btn" href="#">View Our Menu</a>
    </div>
  </section>

  <section class="location">
    <div class="map" role="img" aria-label="Street map showing the bar's location"></div>
    <div class="location-copy">
      <h2>Location</h2>
      <div class="phone">(555) 250-0134</div>
      <address>4200 Harbor Ave, Suite 12, Hoboken, NJ 07030</address>
      <a class="btn" href="https://qelmo.com">Reservation Now</a>
    </div>
  </section>

  <footer class="footer">
    <div class="footer-frame">
      <ul class="footer-links">
        <li>Home</li><li>Menu</li><li>Contact</li><li>Reservations</li>
      </ul>
      <div class="footer-brand"><span class="name">Velvet Lantern</span></div>
      <div class="footer-social">
        <div>Connect with us</div>
        <div class="icons"><span></span><span></span><span></span></div>
        <div class="copy">© 2023 Velvet Lantern</div>
      </div>
    </div>
  </footer>

</div>
</body>
</html>
```